Silver Creek Plumbing Business card & letter head design

We need a new business card and letter head for our plumbing company called silver creek plumbing. attached is the companys logo. We provide domestic and commercial plumbing services in regional western Australia. We are after Something simple yet nice to look at and something that fits within the trade industry.

Target Market(s)

trade/building industry

Contact Information for Business Card

Darl Hensby
Manager
0461 238 574
enquiries@scplumbwork.net.au
ABN: 47 381 905 462
PCL: 5187

Domestic & Commercial Plumbing
Tip Truck & Excavator hire

Colors

Designer to choose colors to be used in the design.

```html
<!DOCTYPE html>
<html lang="en">
<head>
<meta charset="utf-8">
<title>Silver Creek Plumbing – Stationery</title>
<link rel="stylesheet" href="https://fonts.googleapis.com/css2?family=Roboto:wght@300;400;700&display=swap">
<style>
  :root {
    --backdrop: #eef1f5;
    --paper: #e2effd;
    --tint: #c5e1fb;
    --brand-blue: #0c58a6;
    --steel-grey: #adadad;
    --rule-dark: #0b2344;
    --ink: #1c3a63;
  }
  * { box-sizing: border-box; margin: 0; padding: 0; }
  html, body { width: 1200px; height: 1200px; overflow: hidden; }
  body {
    background: var(--backdrop);
    font-family: "Roboto", sans-serif;
    color: var(--ink);
    position: relative;
  }
  .brand-name {
    font-family: "Roboto", sans-serif;
    font-weight: 700;
    color: var(--brand-blue);
    text-transform: uppercase;
    white-space: nowrap;
    letter-spacing: 0.02em;
  }

  /* Letterhead */
  .letterhead {
    position: absolute; left: 70px; top: 190px;
    width: 570px; height: 806px;
    background: var(--paper);
    box-shadow: 0 6px 20px rgba(0,0,0,.18);
    overflow: hidden;
  }
  .letterhead-header {
    position: absolute; left: 0; top: 0; right: 0; height: 80px;
    background: var(--tint);
    border-bottom: 2px solid var(--rule-dark);
  }
  .letterhead-header .brand-name {
    position: absolute; left: 40px; top: 30px; font-size: 15px;
  }
  .letterhead-header .band-blue {
    position: absolute; right: 0; top: 0; width: 270px; height: 44px;
    background: var(--brand-blue);
    clip-path: polygon(14% 0, 100% 0, 100% 100%, 0 100%);
  }
  .letterhead-header .band-grey {
    position: absolute; right: 0; top: 44px; width: 185px; height: 20px;
    background: var(--steel-grey);
    clip-path: polygon(8% 0, 100% 0, 100% 100%, 0 100%);
  }
  .letterhead-footer {
    position: absolute; left: 0; bottom: 0; right: 0; height: 76px;
    background: var(--tint);
  }
  .letterhead-footer .band-grey {
    position: absolute; left: 0; top: 20px; width: 182px; height: 26px;
    background: var(--steel-grey);
    clip-path: polygon(0 0, 100% 0, 88% 100%, 0 100%);
  }
  .letterhead-footer .band-blue {
    position: absolute; left: 0; bottom: 0; width: 265px; height: 30px;
    background: var(--brand-blue);
    clip-path: polygon(0 0, 100% 0, 88% 100%, 0 100%);
  }
  .letterhead-footer .brand-name {
    position: absolute; right: 22px; top: 34px; font-size: 9px;
  }

  /* Business cards */
  .business-card {
    position: absolute; left: 717px; width: 404px; height: 242px;
    background: var(--tint);
    box-shadow: 0 4px 14px rgba(0,0,0,.16);
    overflow: hidden;
  }
  .card-front { top: 378px; }
  .card-back { top: 656px; }
  .card-bottom-bar {
    position: absolute; left: 0; right: 0; bottom: 0; height: 15px;
    background: var(--brand-blue);
  }
  .card-front .band-blue {
    position: absolute; left: 0; top: 0; width: 189px; height: 30px;
    background: var(--brand-blue);
    clip-path: polygon(0 0, 86% 0, 100% 100%, 0 100%);
  }
  .card-front .band-grey {
    position: absolute; left: 0; top: 30px; width: 130px; height: 14px;
    background: var(--steel-grey);
    clip-path: polygon(0 0, 91% 0, 100% 100%, 0 100%);
  }
  .card-front .brand-name {
    position: absolute; left: 0; right: 0; top: 106px;
    text-align: center; font-size: 22px;
  }

  .card-back-header {
    position: absolute; left: 0; right: 0; top: 0; height: 45px;
    border-bottom: 1.5px solid var(--rule-dark);
  }
  .card-back-header .brand-name {
    position: absolute; left: 14px; top: 17px; font-size: 8px;
  }
  .card-back-header .band-blue {
    position: absolute; right: 0; top: 0; width: 189px; height: 30px;
    background: var(--brand-blue);
    clip-path: polygon(14% 0, 100% 0, 100% 100%, 0 100%);
  }
  .card-back-header .band-grey {
    position: absolute; right: 0; top: 30px; width: 130px; height: 14px;
    background: var(--steel-grey);
    clip-path: polygon(9% 0, 100% 0, 100% 100%, 0 100%);
  }
  .services {
    position: absolute; left: 0; right: 0; top: 49px;
    text-align: center; font-size: 11px; font-weight: 300; color: var(--ink);
  }
  .contact-person {
    position: absolute; left: 20px; width: 135px; top: 133px; text-align: center;
  }
  .contact-person .person-name { font-size: 19px; font-weight: 300; }
  .contact-person .person-role {
    display: flex; align-items: center; justify-content: center; gap: 3px;
    font-size: 8.5px; margin-top: 2px;
  }
  .contact-person .person-role::before,
  .contact-person .person-role::after {
    content: ""; width: 20px; height: 1px; background: var(--ink);
  }
  .divider {
    position: absolute; left: 175px; top: 92px; width: 1.5px; height: 114px;
    background: var(--rule-dark);
  }
  .contact-details {
    position: absolute; left: 202px; top: 112px;
    list-style: none; font-size: 13px; font-weight: 300; line-height: 20px;
  }
</style>
</head>
<body>

  <section class="letterhead" aria-label="Letterhead">
    <header class="letterhead-header">
      <div class="band-blue"></div>
      <div class="band-grey"></div>
      <span class="brand-name">Silver Creek Plumbing</span>
    </header>
    <footer class="letterhead-footer">
      <div class="band-grey"></div>
      <div class="band-blue"></div>
      <span class="brand-name">Silver Creek Plumbing</span>
    </footer>
  </section>

  <section class="business-card card-front" aria-label="Business card front">
    <div class="band-blue"></div>
    <div class="band-grey"></div>
    <span class="brand-name">Silver Creek Plumbing</span>
    <div class="card-bottom-bar"></div>
  </section>

  <section class="business-card card-back" aria-label="Business card back">
    <header class="card-back-header">
      <span class="brand-name">Silver Creek Plumbing</span>
      <div class="band-blue"></div>
      <div class="band-grey"></div>
    </header>
    <p class="services">Domestic &amp; Commercial Plumbing • Tip Truck &amp; Excavator hire</p>
    <div class="contact-person">
      <p class="person-name">Darl Hensby</p>
      <p class="person-role">Manager</p>
    </div>
    <div class="divider"></div>
    <ul class="contact-details">
      <li>0461 238 574</li>
      <li>enquiries@scplumbwork.net.au</li>
      <li>ABN: 47 381 905 462</li>
      <li>PCL: 5187</li>
    </ul>
    <div class="card-bottom-bar"></div>
  </section>

</body>
</html>
```